The Winslowe is the building name it is a luxury Coop in the city .

I manage a Coop in the City and need a business card that is simple but sharpe. I read architectural drawing, manage a full service building staff, we make repairs , we order supplies, etc . I need a card and a logo design the reflex what we do here and I am open to options . Colors blue , grey , stainlesss steel . Options thx

Industry/Entity Type

Property Management

Contact Information for Business Card

"The Winslowe " is the building name I think it should be on one side and all
Other information on the next .

Font styles to use
Serif

Requirements
Must have
• Building name "The Winslowe "
• My name Rob Tavener
• My email ROB41W8THAV@QUILLMAIL.COM
• Cell 646-318-5572
• Work 212-614-7790
• Fax 212-614-3158
Nice to have
• Maybe a drawing picture and tools something to that effect .

```html
<!DOCTYPE html>
<html lang="en">
<head>
<meta charset="utf-8">
<title>The Winslowe – Business Card</title>
<link href="https://fonts.googleapis.com/css2?family=Lato:wght@400;700;900&display=swap" rel="stylesheet">
<style>
  :root {
    --page-bg: #e4e5e7;
    --card-white: #ffffff;
    --card-dark: #3a3b3e;
    --brand-blue: #1c4a9e;
    --text-dark: #2b2b2d;
    --band-dark: #3a3b3e;
  }
  * { box-sizing: border-box; margin: 0; padding: 0; }
  html, body {
    width: 1200px; height: 900px; overflow: hidden;
    background: var(--page-bg);
    font-family: "Lato", Arial, sans-serif;
  }
  .canvas {
    width: 1200px; height: 900px;
    display: flex; flex-direction: column;
    align-items: center; justify-content: center; gap: 44px;
  }
  .card {
    position: relative;
    width: 630px; height: 360px;
    border-radius: 4px;
    overflow: hidden;
    box-shadow: 0 8px 22px rgba(0,0,0,.18);
  }
  .card-back {
    background: var(--card-dark);
    display: flex; align-items: center; justify-content: center;
  }
  .card-back .building-name {
    color: var(--brand-blue);
    font-weight: 900;
    font-size: 62px;
    letter-spacing: -1px;
  }
  .card-front { background: var(--card-white); }
  .bottom-band {
    position: absolute; left: 0; top: 0;
    width: 630px; height: 360px;
  }
  .card-front .building-name {
    position: absolute; left: 36px; top: 30px;
    color: var(--brand-blue);
    font-weight: 900;
    font-size: 52px;
    letter-spacing: -1px;
  }
  .contact-block {
    position: absolute; left: 36px; top: 116px;
    color: var(--text-dark);
    font-size: 15px; line-height: 1.4;
  }
  .address { margin-bottom: 3px; padding-left: 22px; }
  .contact-line { display: flex; align-items: center; gap: 8px; }
  .contact-line svg { width: 14px; height: 14px; flex: none; fill: var(--brand-blue); }
  .person {
    position: absolute; left: 392px; top: 212px;
  }
  .person-name {
    color: var(--brand-blue);
    font-weight: 700; font-size: 27px;
  }
  .person-title {
    color: var(--text-dark);
    font-size: 18px;
  }
</style>
</head>
<body>
<main class="canvas">

  <section class="card card-back" aria-label="Card back">
    <h1 class="building-name">The Winslowe</h1>
  </section>

  <section class="card card-front" aria-label="Card front">
    <svg class="bottom-band" viewBox="0 0 630 360" aria-hidden="true">
      <path d="M0 284 C 200 312, 420 342, 630 368 L 630 360 L 0 360 Z" fill="var(--band-dark)"/>
      <path d="M250 300 C 420 318, 540 336, 630 346 L 630 354 C 540 344, 420 326, 250 300 Z" fill="var(--brand-blue)"/>
    </svg>

    <h2 class="building-name">The Winslowe</h2>

    <div class="contact-block">
      <p class="address">41 West 8th Ave<br>New York, NY 10011</p>
      <p class="contact-line">
        <svg viewBox="0 0 24 24" aria-label="Work phone"><path d="M6.6 10.8a15 15 0 0 0 6.6 6.6l2.2-2.2c.3-.3.7-.4 1-.2 1.1.4 2.3.6 3.6.6.6 0 1 .4 1 1V20c0 .6-.4 1-1 1A17 17 0 0 1 3 4c0-.6.4-1 1-1h3.5c.6 0 1 .4 1 1 0 1.3.2 2.5.6 3.6.1.3 0 .7-.2 1z"/></svg>
        212-614-7790
      </p>
      <p class="contact-line">
        <svg viewBox="0 0 24 24" aria-label="Cell phone"><path d="M7 1h10a2 2 0 0 1 2 2v18a2 2 0 0 1-2 2H7a2 2 0 0 1-2-2V3a2 2 0 0 1 2-2zm0 3v14h10V4z"/></svg>
        646-318-5572
      </p>
      <p class="contact-line">
        <svg viewBox="0 0 24 24" aria-label="Fax"><path d="M6 2h12v6H6zM3 9h18a1 1 0 0 1 1 1v7h-4v5H6v-5H2v-7a1 1 0 0 1 1-1zm5 7v4h8v-4z"/></svg>
        212-614-3158
      </p>
      <p class="contact-line">
        <svg viewBox="0 0 24 24" aria-label="Email"><path d="M2 5h20v14H2zm2 2v.5l8 5 8-5V7z"/></svg>
        ROB41W8THAV@QUILLMAIL.COM
      </p>
    </div>

    <div class="person">
      <p class="person-name">Rob Tavener</p>
      <p class="person-title">Superintendent</p>
    </div>
  </section>

</main>
</body>
</html>
```